Produkt-Etiketten-Design für Wagyu-Bolognese-Sauce
Sehr schnell, sehr hilfsbereit und Änderungen sehr schnell umgesetzt...verdient die 5 Sterne
Zielgruppe
Wir sind ein landwirtschaftliches Unternehmen und züchten Wagyu Rinder und betreiben einen Online Shop.
Unsere Produktpallete beinhaltet Tk und frisch Fleisch und nun wollen wir unser Palette um Convinienc Food erweitern und dafür brauchen wir Etiketten.
Aufgabenstellung
Es sollte optisch zu unserem webauftritt und unserer Linie passen.
Wir brauchen Produkt Etikett für Wagyu Bolognese Sauce.
Gläser Maße hier entnehmen - https://www.vorratika.com/rundglas-435ml-klarglas-rtx.-bq17-kiste-64stk.html
Wir bauchen auch eine Zutaten-und Nährwerttabelle

```html
<!DOCTYPE html>
<html lang="de">
<head>
<meta charset="utf-8">
<title>Lindhof Farm – Wagyu Bolognese Sauce Etikett</title>
<link rel="stylesheet" href="https://fonts.googleapis.com/css2?family=Alegreya+Sans:ital,wght@0,400;1,300;1,400&family=Bodoni+Moda:ital,wght@0,400;1,400&family=Fira+Sans:wght@700&family=Roboto:wght@300;400;700&display=swap">
<style>
  :root {
    --page-bg: #dcdcdc;
    --label-bg: #f4f4f4;
    --brand-red: #a51b32;
    --ink: #1a1a1a;
    --ink-soft: #555555;
    --rule: #2a2a2a;
    --illustration-tone: #e4e2e2;
  }
  * { box-sizing: border-box; margin: 0; padding: 0; }
  html, body { width: 1200px; height: 887px; overflow: hidden; }
  body { background: var(--page-bg); position: relative; font-family: "Roboto", sans-serif; color: var(--ink); }

  .label {
    position: absolute; left: 30px; top: 167px;
    width: 1140px; height: 553px;
    background: var(--label-bg);
  }
  .abs { position: absolute; }

  /* back panel: story */
  .story-title {
    left: 36px; top: 36px;
    font-family: "Alegreya Sans", sans-serif; font-style: italic; font-weight: 400;
    font-size: 23px; line-height: 28px; color: var(--brand-red);
  }
  .story-text {
    left: 36px; top: 114px; width: 276px;
    font-weight: 300; font-size: 13.5px; line-height: 21.8px; text-align: justify;
    hyphens: auto; -webkit-hyphens: auto;
  }
  .story-text p + p { margin-top: 9px; }

  .brand-back { left: 37px; top: 440px; }
  .brand-name {
    font-family: "Roboto", sans-serif; font-weight: 700; font-size: 26px;
    color: var(--brand-red); letter-spacing: 0.5px; line-height: 30px;
  }
  .brand-tagline {
    font-family: "Alegreya Sans", sans-serif; font-size: 15.5px; color: var(--ink-soft); line-height: 20px;
  }
  .brand-url { margin-top: 8px; font-weight: 300; font-size: 15px; color: var(--brand-red); }

  /* back panel: nutrition */
  .nutrition { left: 408px; top: 44px; width: 182px; font-size: 15px; }
  .nutrition table { width: 100%; border-collapse: collapse; }
  .nutrition th, .nutrition td { white-space: nowrap; font-weight: 300; }
  .nutrition th { text-align: left; height: 27px; padding: 0 0 5px 1px; border-bottom: 1px solid var(--rule); vertical-align: bottom; }
  .nutrition th:last-child, .nutrition td:last-child { text-align: right; }
  .nutrition td { height: 27px; padding: 0 2px 2px; border-bottom: 1px solid var(--rule); vertical-align: bottom; }
  .nutrition tr.first td { height: 33px; }
  .nutrition tr:last-child td { border-bottom: none; }

  .content-size { left: 400px; top: 330px; width: 196px; text-align center; text-align: center; font-weight: 300; font-size: 30px; line-height: 36px; white-space: nowrap; }
  .best-before-note { left: 355px; top: 380px; width: 290px; text-align: center; font-weight: 300; font-size: 10.5px; }
  .best-before-box { left: 375px; top: 395px; width: 250px; height: 60px; border: 1px solid #888; background: #fafafa; }
  .producer { left: 375px; top: 462px; width: 250px; text-align: center; font-weight: 300; font-size: 19px; line-height: 22px; }

  /* front panel */
  .brand-vertical {
    left: 760px; top: 541px;
    transform: rotate(-90deg); transform-origin: 0 0;
    width: 521px; text-align: center;
    font-family: "Roboto", sans-serif; font-weight: 700; font-size: 54px; line-height: 54px;
    letter-spacing: 4px; color: var(--brand-red); white-space: nowrap;
  }
  .cow-illustration { left: 1001px; top: 29px; width: 128px; height: 222px; background: var(--illustration-tone); }
  .product-meat {
    right: 10px; top: 240px;
    font-family: "Fira Sans", sans-serif; font-weight: 700; font-size: 84px; line-height: 90px;
    color: var(--brand-red); letter-spacing: -2px;
  }
  .product-name {
    right: 7px; top: 381px; font-family: "Bodoni Moda", serif; font-size: 64px; line-height: 70px; letter-spacing: -3px;
  }
  .product-type {
    left: 925px; top: 438px; font-family: "Bodoni Moda", serif; font-style: italic; font-size: 66px; line-height: 72px; letter-spacing: -3px;
  }
  .slogan {
    right: 10px; top: 516px;
    font-family: "Alegreya Sans", sans-serif; font-style: italic; font-weight: 300; font-size: 21px; color: var(--brand-red);
  }
</style>
</head>
<body>
  <div class="label">
    <h2 class="abs story-title">Qualität vom<br>diplomierten Fleischsommelier</h2>
    <div class="abs story-text">
      <p>Unsere Vision ist seit Beginn qualitativ hochwertige Produkte herzustellen, mit dem Augenmerk das Tier mit Respekt und Sorgfalt zu behandeln! Seit 2017 darf ich mich zu den Diplomierten Fleischsommeliers zählen.</p>
      <p>Unser Leitspruch „Genuss ist eine Lebenseinstellung“ bezieht sich nicht nur auf den Teller, auch der Lebensgenuss unserer Tiere ist uns sehr wichtig.</p>
      <p>Unser Wagyu Hackfleisch wird mit 4 mm gewolft und hat einen idealen Fettanteil.</p>
    </div>

    <div class="abs brand-back">
      <div class="brand-name">LINDHOF FARM</div>
      <div class="brand-tagline">Wagyu Rinder – unsere Passion</div>
      <div class="brand-url">www.lindhof-rinder.com/shop/</div>
    </div>

    <div class="abs nutrition">
      <table>
        <thead><tr><th>Nährwerte</th><th>Pro 100 g</th></tr></thead>
        <tbody>
          <tr class="first"><td>Energie</td><td>281 kj</td></tr>
          <tr><td>Fett</td><td>4 g</td></tr>
          <tr><td>Davon gesättigte</td><td></td></tr>
          <tr><td>Fettsäuren</td><td>0,4 g</td></tr>
          <tr><td>Kohlenhydrate</td><td>5,7 g</td></tr>
          <tr><td>davon Zucker</td><td>4 g</td></tr>
          <tr><td>Ballaststoffe</td><td>1,8 g</td></tr>
          <tr><td>Eiweiss</td><td>1,3 g</td></tr>
          <tr><td>Salz</td><td>1 g</td></tr>
        </tbody>
      </table>
    </div>
    <div class="abs content-size">Inhalt 380 ml</div>
    <div class="abs best-before-note">Bei Zimmertemperatur mindestens haltbar bis:</div>
    <div class="abs best-before-box"></div>
    <div class="abs producer">Lindhof Farm Kft<br>8812 Almavölgy<br>Ungarn</div>

    <div class="abs brand-vertical">LINDHOF FARM</div>
    <div class="abs cow-illustration" role="img" aria-label="Linienzeichnung eines Wagyu-Rinderkopfes"></div>
    <div class="abs product-meat">Wagyu</div>
    <div class="abs product-name">Bolognese</div>
    <div class="abs product-type">Sauce</div>
    <div class="abs slogan">Genuss ist eine Lebenseinstellung</div>
  </div>
</body>
</html>
```